依頼詳細
PCとスマホデザインの両方納品をいただきますが、
まずはデザインイメージが確認しやすいPCページのみの提案をお願いします。
スマホページは当選者に納品時にお願いしたいと思います。
スマホサイズについて、カンバスサイズは横幅375pxで作成し、2倍の横幅750pxのサイズで書き出ししてください。
(Retinaディスプレイに対応するため)
スマホページ作成時は、メニューが展開した際のデザインもお願いします。
レスポンシブウェブデザインを意識したデザインでお願いします。

■サイトマップ
添付の画面遷移図をご確認ください。

■参考サイト
https://harbor-mend-crew.com/
https://www.qv-tm.co.jp/

■内容について
工場や倉庫の修繕・改修・増築などを専門とするサービスサイトになります。

■素材写真
画像データについては、フリー素材から流用して
イメージ画像に当て込んでください。
足りない場合は、一旦他のサイトの写真をサンプルとして
入れてください。(サンプルなどの表記をお願いします)
また、購入が必要な写真などを利用した場合、
価格とサイト名を教えてください。

また、Nimbrel Stockで定期契約をしていますので、
Nimbrel Stockの画像は使用できます。
デザイン時はカンプ画像をお入れいただきますようお願いします。

■ロゴについて
添付のロゴデータを使用してください。

■ワイヤーフレーム
https://mk.velquora.com/view/600e5e1a-e3bd-4b32-a74b-244a4501d661-355d/?fullscreen
コンテンツの構成としてワイヤーフレームを作成しましたが
必ずしもワイヤーフレームの通りではなくて大丈夫です。
TOPページに配置するコンテンツを見ていただき、デザインは
デザイナーの皆様におまかせしたいと思います。

----------------------------------------------------------------------------
【制作物に対するお願い】

■フォントについて
・無料で使えるフォントで作成をお願いします。
・OSに紐づくフォントの使用は控えていただければと思います (ヒラギノなど)

サイトURL
ページ数
1ページ
希望イメージ
シンプル 複雑
単色 カラフル
暗い 明るい
日常 高級
遊び心 厳粛
未来的 伝統的
女性的 男性的
希望する色
ベースカラー:白、ポイントカラー:赤、青(救急のイメージ)
納品ファイル
• 高解像度JPG (.jpg)
• イラストレーター形式 (.ai)
• フォトショップ形式 (.psd)
補足説明
上記のいずれか1つ(アウトラインありとなしの2つ)と高解像度JPGを納品お願いします。
adobe XDでの納品も可能です。

```html
<!DOCTYPE html>
<html lang="ja">
<head>
<meta charset="UTF-8">
<title>工場修繕ナビ｜工場倉庫の専門修繕</title>
<link href="https://fonts.googleapis.com/css2?family=Noto+Sans+JP:wght@400;500;700;900&family=Oswald:wght@500;600&display=swap" rel="stylesheet">
<style>
:root{
  --red:#c8202a;
  --blue:#1f6fc1;
  --navy:#173a6a;
  --sky:#dbe9f6;
  --gray:#f0f1f3;
  --ink:#222;
  --muted:#666;
  --line:#d6d9de;
  --white:#fff;
}
*{box-sizing:border-box;margin:0;padding:0}
html,body{width:1200px;height:4160px;overflow:hidden}
body{font-family:"Noto Sans JP",sans-serif;color:var(--ink);background:var(--white);position:relative}
.en{font-family:"Oswald",sans-serif;letter-spacing:.02em}
.ph{display:block}
.brand{display:flex;align-items:center;gap:10px;font-weight:900;color:var(--navy)}
.brand .mark{width:14px;height:14px;background:var(--red)}
.btn{display:inline-flex;align-items:center;justify-content:center;gap:10px;border-radius:24px;font-weight:700;font-size:14px;color:var(--white)}
.btn-blue{background:var(--blue)}
.btn-red{background:var(--red)}
.btn-outline{border:1px solid var(--red);color:var(--red);background:var(--white)}
.arrow{display:inline-block;width:14px;height:1px;background:currentColor;position:relative}
.arrow::after{content:"";position:absolute;right:0;top:-3px;width:6px;height:6px;border-top:1px solid currentColor;border-right:1px solid currentColor;transform:rotate(45deg)}

/* header */
.site-header{height:150px;position:relative;border-bottom:1px solid var(--line)}
.site-header .brand{position:absolute;left:30px;top:26px;font-size:26px}
.util{position:absolute;right:30px;top:22px;display:flex;align-items:center;gap:22px;font-size:13px}
.util .tel{display:flex;align-items:center;gap:8px;font-size:28px;font-weight:700;color:var(--navy)}
.util .btn{height:46px;padding:0 20px;font-size:13px}
.gnav{position:absolute;left:0;right:0;top:100px;display:flex;justify-content:center;gap:0;font-size:14px;font-weight:500}
.gnav a{padding:6px 26px;border-left:1px solid var(--line);color:var(--ink);text-decoration:none}
.gnav a:last-child{border-right:1px solid var(--line)}

/* hero */
.hero{height:440px;position:relative;overflow:hidden}
.hero .ph{position:absolute;inset:0;background:linear-gradient(100deg,#cfe0f1 0%,#eef4fa 45%,#b9c9da 100%)}
.hero-copy{position:absolute;left:330px;top:110px;text-align:center}
.hero-copy .brand{font-size:56px;justify-content:center}
.hero-copy .brand .mark{width:40px;height:40px}
.hero-copy .tag{margin-top:30px;display:inline-block;background:var(--white);padding:14px 34px;border-radius:40px;font-size:26px;font-weight:900;color:var(--navy);box-shadow:0 4px 14px rgba(0,0,0,.12)}
.hero-copy .tag em{font-style:normal;color:var(--blue)}

/* feature */
.feature{position:relative;height:690px}
.feature .title{position:absolute;left:165px;top:85px;font-size:64px;color:var(--red);line-height:1}
.feature .sub{position:absolute;left:165px;top:160px;font-size:24px;font-weight:900}
.feature .body{position:absolute;left:165px;top:220px;width:500px;font-size:12.5px;line-height:2;color:#333}
.feature .body p+p{margin-top:14px}
.feature .btn{position:absolute;left:165px;top:480px;width:150px;height:44px}
.feature .ph1{position:absolute;left:720px;top:125px;width:310px;height:300px;background:linear-gradient(160deg,#c8d2dc,#8e9eb0)}
.feature .ph2{position:absolute;left:790px;top:430px;width:250px;height:240px;background:linear-gradient(160deg,#e4ebf2,#6f88a6)}

/* works */
.works{position:relative;height:640px}
.works .bg{position:absolute;left:0;right:0;top:60px;height:580px;background:linear-gradient(180deg,#5f7fa8,#2f4f7d)}
.works .panel{position:absolute;left:165px;top:0;width:870px;height:500px;background:var(--white);border-radius:8px;box-shadow:0 6px 20px rgba(0,0,0,.15);padding:30px 40px}
.sec-head{display:flex;align-items:center;gap:14px}
.sec-head h2{font-size:50px;color:var(--red);line-height:1;font-weight:600}
.sec-head .jp{font-size:13px;font-weight:700}
.sec-head .mascot{width:36px;height:36px;border-radius:50%;background:var(--blue)}
.works .more{position:absolute;right:40px;top:44px;width:230px;height:36px}
.work-list{display:flex;gap:28px;margin-top:30px}
.work{width:250px;text-align:center;font-size:13px}
.work .ph{height:180px;background:linear-gradient(180deg,#bcd3ec,#e3e8ee 60%,#9aa3ad)}
.work p{margin-top:18px;line-height:1.6}
.work .btn{margin-top:16px;width:150px;height:36px;font-size:13px}

/* column */
.column{position:relative;height:580px;padding:110px 165px 0}
.column .more{position:absolute;right:165px;top:118px;width:230px;height:36px}
.col-grid{display:grid;grid-template-columns:1fr 1fr;gap:40px 40px;margin-top:44px}
.col-item{display:flex;gap:20px}
.col-item .ph{width:150px;height:110px;flex:none;background:linear-gradient(150deg,#d6dde5,#7f94ac)}
.col-item time{font-size:11px;color:var(--muted)}
.col-item h3{font-size:14px;color:var(--red);line-height:1.5;margin-top:4px}
.col-item p{font-size:11px;color:var(--muted);line-height:1.7;margin-top:6px}
.col-item .more-link{font-size:10px;color:var(--red);text-align:right;margin-top:4px;font-weight:700}

/* news */
.news{height:520px;background:var(--gray);position:relative;padding:85px 165px 0}
.news .sec-head{flex-direction:column;align-items:flex-start;gap:6px}
.news-list{position:absolute;left:400px;top:85px;width:635px}
.news-item{padding:24px 0;border-bottom:1px solid var(--line);font-size:13px}
.news-item time{display:block;color:var(--red);font-weight:700;margin-bottom:6px}
.news .more-row{position:absolute;left:165px;top:315px;display:flex;align-items:center;gap:18px;font-size:12px}
.circle{width:44px;height:44px;border:1px solid var(--red);border-radius:50%;display:flex;align-items:center;justify-content:center;color:var(--red);background:var(--white)}

/* contents */
.contents{height:430px;text-align:center;padding-top:85px}
.contents .sec-head{justify-content:center}
.cards{display:flex;justify-content:center;gap:30px;margin-top:40px}
.card{width:270px}
.card .ph{height:140px}
.card .label{height:52px;display:flex;align-items:center;justify-content:center;gap:12px;color:var(--white);font-weight:700;font-size:15px}
.card:nth-child(1) .ph{background:linear-gradient(150deg,#c9a57a,#7c5b3c)}
.card:nth-child(2) .ph{background:linear-gradient(150deg,#e6e2da,#8b8f96)}
.card:nth-child(3) .ph{background:linear-gradient(150deg,#cfd8e2,#5b6f88)}
.card:nth-child(1) .label,.card:nth-child(3) .label{background:var(--red)}
.card:nth-child(2) .label{background:var(--blue)}

/* contact */
.contact{height:410px;background:#e9eef4;position:relative;padding:75px 165px 0}
.contact .lead{position:absolute;left:615px;top:92px;font-size:13px}
.contact-boxes{display:flex;gap:40px;margin-top:40px;justify-content:center}
.cbox{width:370px;height:110px;background:var(--white);border:2px solid var(--red);border-radius:4px;display:flex;flex-direction:column;align-items:center;justify-content:center;gap:6px}
.cbox .small{font-size:11px}
.cbox .tel{display:flex;align-items:center;gap:8px;font-size:32px;font-weight:700;color:var(--navy)}
.cbox .btn{width:300px;height:44px}
.to-top{position:absolute;right:100px;top:3745px;width:56px;height:56px;border-radius:50%;background:var(--red);display:flex;align-items:center;justify-content:center;z-index:2}

/* footer */
.site-footer{height:390px;background:var(--blue);color:var(--white);position:relative}
.site-footer .brand{position:absolute;left:110px;top:85px;font-size:32px;color:var(--white)}
.site-footer .brand .mark{background:var(--white)}
.site-footer .tel{position:absolute;left:110px;top:150px;font-size:30px;font-weight:700;display:flex;align-items:center;gap:8px}
.site-footer .legal{position:absolute;left:110px;top:200px;font-size:12px}
.fnav{position:absolute;left:560px;top:80px;display:flex;gap:60px;font-size:12px;line-height:2.3}
.fnav ul{list-style:none}
.copy{position:absolute;left:560px;top:295px;font-size:10px;opacity:.85}
</style>
</head>
<body>

<header class="site-header">
  <div class="brand"><span class="mark"></span>工場修繕ナビ</div>
  <div class="util">
    <span>会社概要</span><span>よくある質問</span>
    <span class="tel"><svg width="24" height="24" viewBox="0 0 24 24"><path fill="#173a6a" d="M6.6 10.8a15 15 0 006.6 6.6l2.2-2.2a1 1 0 011-.25 11 11 0 003.6.6 1 1 0 011 1V20a1 1 0 01-1 1A17 17 0 013 4a1 1 0 011-1h3.5a1 1 0 011 1c0 1.25.2 2.45.6 3.6a1 1 0 01-.25 1z"/></svg>0570-55-3981</span>
    <span class="btn btn-red">カタログダウンロード</span>
    <span class="btn btn-blue">無料お見積り</span>
  </div>
  <nav class="gnav">
    <a>ホーム</a><a>工場修繕ナビの特徴</a><a>サービス一覧</a><a>施工実績</a><a>お問い合わせ</a>
  </nav>
</header>

<section class="hero">
  <div class="ph" role="img" aria-label="工場倉庫の外観と点検作業員の写真"></div>
  <div class="hero-copy">
    <div class="brand"><span class="mark"></span>工場修繕ナビ</div>
    <div class="tag"><em>工場倉庫の専門修繕</em>はおまかせください！</div>
  </div>
</section>

<section class="feature">
  <h2 class="title en">FEATURE</h2>
  <p class="sub">工場専門修繕サービス</p>
  <div class="body">
    <p>工場修繕ナビについて説明文が入ります。修繕から改修、増築まで一貫して対応いたします。工場や倉庫の稼働を止めない施工計画をご提案します。</p>
    <p>工場修繕ナビについて説明文が入ります。屋根や外壁、床面の劣化など、現地調査をもとに最適な修繕方法をわかりやすくご案内します。</p>
    <p>工場修繕ナビについて説明文が入ります。緊急時にも迅速に駆けつけ、安全な作業で建物を守ります。</p>
  </div>
  <span class="btn btn-blue">詳しく見る <i class="arrow"></i></span>
  <div class="ph ph1" role="img" aria-label="足場が組まれた倉庫の修繕現場の写真"></div>
  <div class="ph ph2" role="img" aria-label="図面を確認する作業員の手元の写真"></div>
</section>

<section class="works">
  <div class="bg" role="img" aria-label="倉庫内部の写真"></div>
  <div class="panel">
    <div class="sec-head"><h2 class="en">WORKS</h2><span class="jp">施工実績</span><span class="mascot" role="img" aria-label="マスコットキャラクター"></span></div>
    <span class="btn btn-blue more">施工実績一覧 <i class="arrow"></i></span>
    <div class="work-list">
      <div class="work"><div class="ph" role="img" aria-label="施工後の工場外観の写真"></div><p>株式会社〇〇〇〇<br>工場補修工事</p><span class="btn btn-outline">詳しく見る <i class="arrow"></i></span></div>
      <div class="work"><div class="ph" role="img" aria-label="施工後のプラント外観の写真"></div><p>株式会社〇〇〇〇<br>工場補修工事</p><span class="btn btn-outline">詳しく見る <i class="arrow"></i></span></div>
      <div class="work"><div class="ph" role="img" aria-label="施工後の倉庫外観の写真"></div><p>株式会社〇〇〇〇<br>工場補修工事</p><span class="btn btn-outline">詳しく見る <i class="arrow"></i></span></div>
    </div>
  </div>
</section>

<section class="column">
  <div class="sec-head"><h2 class="en">COLUMN</h2><span class="jp">コラム</span><span class="mascot" role="img" aria-label="マスコットキャラクター"></span></div>
  <span class="btn btn-blue more">コラム一覧 <i class="arrow"></i></span>
  <div class="col-grid">
    <article class="col-item"><div class="ph" role="img" aria-label="点検する作業員の写真"></div><div><time>2024.01.18</time><h3>タイトルが入ります。タイトルが入ります。タイトルが入ります。</h3><p>記事の内容の一部が表示されます。記事の内容の一部が表示されます。</p><div class="more-link">MORE →</div></div></article>
    <article class="col-item"><div class="ph" role="img" aria-label="倉庫の棚の写真"></div><div><time>2024.01.18</time><h3>タイトルが入ります。タイトルが入ります。タイトルが入ります。</h3><p>記事の内容の一部が表示されます。記事の内容の一部が表示されます。</p><div class="more-link">MORE →</div></div></article>
    <article class="col-item"><div class="ph" role="img" aria-label="工場外壁の写真"></div><div><time>2024.01.18</time><h3>タイトルが入ります。タイトルが入ります。タイトルが入ります。</h3><p>記事の内容の一部が表示されます。記事の内容の一部が表示されます。</p><div class="more-link">MORE →</div></div></article>
    <article class="col-item"><div class="ph" role="img" aria-label="倉庫内部の写真"></div><div><time>2024.01.18</time><h3>タイトルが入ります。タイトルが入ります。タイトルが入ります。</h3><p>記事の内容の一部が表示されます。記事の内容の一部が表示されます。</p><div class="more-link">MORE →</div></div></article>
  </div>
</section>

<section class="news">
  <div class="sec-head"><h2 class="en">NEWS</h2><span class="jp">お知らせ</span></div>
  <div class="more-row"><span>お知らせ一覧</span><span class="circle"><i class="arrow"></i></span></div>
  <div class="news-list">
    <div class="news-item"><time>2024.01.01</time>こちらにテキストが入ります。テキストテキストテキストテキストテキスト。</div>
    <div class="news-item"><time>2024.01.01</time>こちらにテキストが入ります。テキストテキストテキストテキストテキスト。</div>
    <div class="news-item"><time>2024.01.01</time>こちらにテキストが入ります。テキストテキストテキストテキストテキスト。</div>
  </div>
</section>

<section class="contents">
  <div class="sec-head"><h2 class="en">CONTENTS</h2><span class="jp">コンテンツ</span><span class="mascot" role="img" aria-label="マスコットキャラクター"></span></div>
  <div class="cards">
    <div class="card"><div class="ph" role="img" aria-label="質問と回答を表す積み木の写真"></div><div class="label">よくある質問 <i class="arrow"></i></div></div>
    <div class="card"><div class="ph" role="img" aria-label="打ち合わせ中のノートパソコンの写真"></div><div class="label">打ち合わせの流れ <i class="arrow"></i></div></div>
    <div class="card"><div class="ph" role="img" aria-label="カタログ冊子の写真"></div><div class="label">カタログダウンロード <i class="arrow"></i></div></div>
  </div>
</section>

<section class="contact">
  <div class="sec-head"><h2 class="en">CONTACT</h2><span class="jp">お問い合わせ</span><span class="mascot" role="img" aria-label="マスコットキャラクター"></span></div>
  <p class="lead">ご質問やご相談など、お気軽にお問い合わせください。</p>
  <div class="contact-boxes">
    <div class="cbox">
      <span class="small">お電話でのお問い合わせ　工場修繕ナビ</span>
      <span class="tel"><svg width="26" height="26" viewBox="0 0 24 24"><path fill="#173a6a" d="M6.6 10.8a15 15 0 006.6 6.6l2.2-2.2a1 1 0 011-.25 11 11 0 003.6.6 1 1 0 011 1V20a1 1 0 01-1 1A17 17 0 013 4a1 1 0 011-1h3.5a1 1 0 011 1c0 1.25.2 2.45.6 3.6a1 1 0 01-.25 1z"/></svg>0570-55-3981</span>
      <span class="small">「工場修繕ナビを見た」とお伝えください</span>
    </div>
    <div class="cbox">
      <span class="small">メールでのお問い合わせ</span>
      <span class="btn btn-blue">無料お見積もり・お問い合わせ <i class="arrow"></i></span>
    </div>
  </div>
</section>

<a class="to-top" aria-label="ページ上部へ"><svg width="18" height="18" viewBox="0 0 18 18"><path d="M3 11l6-6 6 6" stroke="#fff" stroke-width="2" fill="none"/></svg></a>

<footer class="site-footer">
  <div class="brand"><span class="mark"></span>工場修繕ナビ</div>
  <div class="tel"><svg width="24" height="24" viewBox="0 0 24 24"><path fill="#fff" d="M6.6 10.8a15 15 0 006.6 6.6l2.2-2.2a1 1 0 011-.25 11 11 0 003.6.6 1 1 0 011 1V20a1 1 0 01-1 1A17 17 0 013 4a1 1 0 011-1h3.5a1 1 0 011 1c0 1.25.2 2.45.6 3.6a1 1 0 01-.25 1z"/></svg>0570-55-3981</div>
  <div class="legal">プライバシーポリシー｜サイトマップ</div>
  <div class="fnav">
    <ul><li>ホーム</li><li>工場修繕ナビの特徴</li><li>施工実績</li><li>よくある質問</li><li>打ち合わせの流れ</li></ul>
    <ul><li>サービス一覧</li><li>– 屋根修繕</li><li>– 外壁修繕</li><li>– 床面改修</li><li>– 増築工事</li></ul>
    <ul><li>会社概要</li><li>コラム</li><li>お知らせ</li><li>無料お見積り・お問い合わせ</li><li>カタログダウンロード</li></ul>
  </div>
  <div class="copy">Copyright © KOJOSHUZEN NAVI All Rights Reserved.</div>
</footer>

</body>
</html>
```